Business Stationery Branding

This is NOT a logo job. We already have one (attached)

Projects that do not follow the color scheme (see logo) will be rejected immediately.

What I need is for someone to create a modern, clean, simple and minimalist branding for the business.

The designs will be 100% and delivery will include all source & vector files.

What I need are:
1. Business Card
2. Letterhead
3. Envelope
4. Invoice
5. Presentation folder
6. Staff / ID Card
7. Compliments slips
8. Notepad cover
9. Note pad
10. Mug design
11. Pen design

```html
<!DOCTYPE html>
<html lang="en">
<head>
<meta charset="utf-8">
<title>Luma Care Services — Stationery</title>
<link href="https://fonts.googleapis.com/css2?family=Cinzel:wght@400;600&family=Open+Sans:wght@400;600;700&display=swap" rel="stylesheet">
<style>
:root{
  --bg:#e6e6e8;
  --paper:#ffffff;
  --pink:#f1c8d2;
  --pink-soft:#f7dfe5;
  --pink-deep:#d79aab;
  --ink:#4a4a4a;
  --ink-soft:#8a8a8a;
  --line:#e5c3cc;
}
*{box-sizing:border-box;margin:0;padding:0}
html,body{width:1200px;height:720px;overflow:hidden;background:var(--bg);font-family:"Open Sans",sans-serif;color:var(--ink)}
.canvas{position:relative;width:1200px;height:720px}
.item{position:absolute;background:var(--paper);box-shadow:0 2px 6px rgba(0,0,0,.12);overflow:hidden}

/* brand lockup */
.brand{display:flex;flex-direction:column;align-items:center;gap:3px;text-align:center}
.brand-mark{width:14px;height:14px;border-radius:50%;background:var(--pink-deep)}
.brand-name{font-family:"Cinzel",serif;font-weight:600;letter-spacing:.06em;color:var(--ink);white-space:nowrap}
.brand-tag{font-family:"Open Sans",sans-serif;font-style:normal;font-weight:400;font-size:5.5px;letter-spacing:.02em;color:var(--ink);white-space:nowrap}
.brand.light .brand-name,.brand.light .brand-tag{color:#fff}
.brand.light .brand-mark{background:#fff}

.address-strip{position:absolute;left:0;right:0;background:var(--pink);font-weight:700;font-size:7px;letter-spacing:.14em;color:var(--ink);display:flex;align-items:center;justify-content:center;white-space:nowrap}

/* folder */
.folder{left:30px;top:30px;width:440px;height:330px;background:var(--pink)}
.folder-pocket{position:absolute;left:0;bottom:0;width:285px;height:110px;background:var(--paper)}
.folder-panel{position:absolute;left:285px;top:0;width:155px;height:330px;background:var(--pink);border-left:1px solid var(--pink-deep)}
.folder .brand{position:absolute;left:210px;top:125px;width:230px}
.folder .brand-name{font-size:14px}
.folder .brand.tl{left:20px;top:22px;width:110px}
.folder .brand.tl .brand-name{font-size:8px}
.folder-contact{position:absolute;left:20px;bottom:18px;font-size:6px;color:var(--ink);letter-spacing:.05em;white-space:nowrap}
.folder .address-strip{left:286px;bottom:0;height:18px;font-size:5px;letter-spacing:.04em;background:var(--paper)}

/* letterhead */
.letterhead{left:560px;top:22px;width:215px;height:292px;padding:14px 16px;font-size:4.5px;line-height:1.6}
.letterhead .brand{position:absolute;left:14px;top:12px;width:90px}
.letterhead .brand-name{font-size:6px}
.lh-contact{position:absolute;right:14px;top:12px;text-align:left;font-size:4px;color:var(--ink)}
.lh-body{position:absolute;left:16px;top:72px;right:16px}
.lh-body p{margin-bottom:6px}
.lh-sign{font-family:"Cinzel",serif;font-size:8px;margin-top:6px}
.letterhead .address-strip{bottom:12px;height:10px;font-size:5px}

/* invoice */
.invoice{left:795px;top:22px;width:220px;height:292px;padding:12px}
.invoice .brand{position:absolute;left:12px;top:14px;width:70px}
.invoice .brand-name{font-size:5px}
.inv-title{position:absolute;right:14px;top:14px;font-size:11px;font-weight:700;letter-spacing:.12em;color:var(--pink-deep)}
.inv-meta{position:absolute;left:12px;right:12px;top:50px;display:flex;gap:8px;font-size:4px}
.inv-meta div{flex:1;border:1px solid var(--line)}
.inv-meta b{display:block;background:var(--pink);padding:1px 3px}
.inv-meta span{display:block;padding:1px 3px}
.inv-table{position:absolute;left:12px;right:12px;top:110px;height:112px;border:1px solid var(--line);border-collapse:collapse;font-size:4px}
.inv-table th{background:var(--pink);text-align:left;padding:2px 3px;height:8px}
.inv-table td{border-left:1px solid var(--line);height:100px}
.inv-totals{position:absolute;right:12px;top:228px;width:70px;font-size:4px}
.inv-totals div{display:flex;justify-content:space-between;border-bottom:1px solid var(--line);padding:1px 2px}
.inv-totals .total{background:var(--pink)}
.inv-foot{position:absolute;left:12px;top:232px;font-size:4px;line-height:1.7}
.invoice .address-strip{bottom:10px;height:10px;font-size:5px}

/* notepad */
.notepad{left:1035px;top:120px;width:135px;height:190px;background:var(--pink)}
.notepad-rings{position:absolute;left:3px;top:6px;bottom:6px;width:5px;background:repeating-linear-gradient(#666 0 2px,transparent 2px 6px)}
.notepad .brand{position:absolute;left:15px;top:60px;width:115px}
.notepad .brand-name{font-size:7px}

/* pen & eraser */
.pen{left:370px;top:370px;width:150px;height:28px;border-radius:8px;background:linear-gradient(90deg,var(--pink) 0 30%,#f4f4f4 30%)}
.pen .brand{position:absolute;left:52px;top:10px;width:90px}
.pen .brand-name{font-size:5px}
.eraser{left:740px;top:342px;width:60px;height:16px;background:linear-gradient(90deg,#f4f4f4 0 60%,var(--pink) 60%)}

/* compliments slip */
.slip{left:30px;top:405px;width:310px;height:125px}
.slip .brand{position:absolute;left:16px;top:20px;width:90px}
.slip .brand-name{font-size:6px}
.slip .address-strip{bottom:18px;height:14px}

/* envelope */
.envelope{left:30px;top:560px;width:310px;height:140px}
.envelope svg{position:absolute;left:0;top:0}
.envelope .brand{position:absolute;left:100px;top:88px;width:110px}
.envelope .brand-name{font-size:9px}

/* staff card */
.staff-card{left:360px;top:410px;width:220px;height:128px;background:var(--pink);border-radius:6px}
.staff-card .brand{position:absolute;left:10px;top:45px;width:200px}
.staff-card .brand-name{font-size:10px}

/* business card */
.biz-card{left:360px;top:570px;width:220px;height:130px}
.biz-card .brand{position:absolute;left:8px;top:48px;width:95px}
.biz-card .brand-name{font-size:7px}
.biz-info{position:absolute;left:108px;top:10px;font-size:5.5px;line-height:1.5}
.biz-info .name{font-size:7.5px;font-weight:600;color:var(--pink-deep);letter-spacing:.04em}
.biz-info .role{font-weight:700;margin-bottom:3px}
.icon-row{display:flex;align-items:center;gap:4px}
.icon-row svg{flex:none}
.biz-card .address-strip{bottom:0;height:16px;font-size:6px}

/* cd sleeve */
.sleeve{left:605px;top:400px;width:245px;height:180px;background:var(--pink)}
.sleeve .brand{position:absolute;left:20px;top:78px;width:180px}
.sleeve .brand-name{font-size:10px}

/* pencil box */
.pencil-box{left:895px;top:345px;width:55px;height:210px;background:linear-gradient(var(--pink) 0 40%,#fff 40%)}
.pencil-box .brand{position:absolute;left:-48px;top:100px;width:150px;transform:rotate(90deg)}
.pencil-box .brand-name{font-size:7px}

/* wide compliments card */
.wide-card{left:605px;top:610px;width:340px;height:90px}
.wide-card .brand{position:absolute;left:20px;top:22px;width:110px}
.wide-card .brand-name{font-size:6px}
.wide-info{position:absolute;left:150px;top:14px;font-size:6px;line-height:1.6}
.wide-info .name{font-weight:700;font-size:7px}
.wide-right{position:absolute;right:16px;top:14px;font-size:6.5px;line-height:1.6}
.wide-card .address-strip{bottom:0;height:14px}

/* carrier bag */
.bag{left:975px;top:350px;width:200px;height:355px;background:linear-gradient(var(--paper) 0 70%,var(--pink) 70%)}
.bag svg.wave{position:absolute;left:0;top:0}
.bag .brand{position:absolute;left:20px;top:135px;width:160px}
.bag .brand-name{font-size:11px}
.bag-contact{position:absolute;top:205px;font-size:4.5px;line-height:1.6}
.bag-contact.left{left:14px}
.bag-contact.right{right:14px;text-align:right}
.bag-slogan{position:absolute;left:0;right:0;bottom:80px;text-align:center;font-weight:700;font-size:7px;letter-spacing:.2em;color:#fff}
.bag-web{position:absolute;left:0;right:0;bottom:64px;text-align:center;font-size:5px;color:#fff}
</style>
</head>
<body>
<main class="canvas">

  <section class="item folder">
    <div class="brand tl"><span class="brand-mark"></span><span class="brand-name">LUMA CARE SERVICES</span></div>
    <div class="folder-pocket">
      <p class="folder-contact">555 201 4410 · hello@lumacare.example · www.lumacare.example</p>
    </div>
    <div class="folder-panel"></div>
    <div class="brand"><span class="brand-mark"></span><span class="brand-name">LUMA CARE SERVICES</span><span class="brand-tag">Kind support, every single day</span></div>
    <div class="address-strip">Harbor Lane 1200 Elm Ridge Suite 18</div>
  </section>

  <section class="item letterhead">
    <div class="brand"><span class="brand-mark"></span><span class="brand-name">LUMA CARE SERVICES</span></div>
    <div class="lh-contact">48 Elm Ridge Road, Northfield<br>555 201 4410<br>555 309 7722<br>hello@lumacare.example<br>www.lumacare.example</div>
    <div class="lh-body">
      <p>March 2024<br>Ms Jane Cole<br>12 River Road, Northfield</p>
      <p>Dear Ms. Cole,</p>
      <p>Thank you for choosing our team. We are glad to support your family with thoughtful daily care and steady, friendly visits.</p>
      <p>Please find the care plan attached. Call us anytime with questions about schedules or services.</p>
      <p>Regards,</p>
      <p class="lh-sign">Dana Whitfield</p>
    </div>
    <div class="address-strip">Harbor Lane 1200 Elm Ridge Suite 18</div>
  </section>

  <section class="item invoice">
    <div class="brand"><span class="brand-mark"></span><span class="brand-name">LUMA CARE SERVICES</span></div>
    <h1 class="inv-title">INVOICE</h1>
    <div class="inv-meta">
      <div><b>Bill To</b><span>Name</span><span>Address</span></div>
      <div><b>Invoice No.</b><span>Date</span><span>Due</span></div>
    </div>
    <table class="inv-table">
      <tr><th>Qty</th><th>Description</th><th>Rate</th><th>Amount</th></tr>
      <tr><td></td><td></td><td></td><td></td></tr>
    </table>
    <div class="inv-foot">Bank Details<br>Thank you for your business</div>
    <div class="inv-totals">
      <div><span>Subtotal</span><span></span></div>
      <div><span>Tax</span><span></span></div>
      <div class="total"><span>Total</span><span></span></div>
    </div>
    <div class="address-strip">Harbor Lane 1200 Elm Ridge Suite 18</div>
  </section>

  <section class="item notepad">
    <div class="notepad-rings"></div>
    <div class="brand light"><span class="brand-mark"></span><span class="brand-name">LUMA CARE SERVICES</span></div>
  </section>

  <section class="item pen">
    <div class="brand"><span class="brand-name">LUMA CARE SERVICES</span></div>
  </section>
  <div class="item eraser"></div>

  <section class="item slip">
    <div class="brand"><span class="brand-mark"></span><span class="brand-name">LUMA CARE SERVICES</span></div>
    <div class="address-strip">Harbor Lane 1200 Elm Ridge Suite 18</div>
  </section>

  <section class="item envelope">
    <svg width="310" height="140" viewBox="0 0 310 140" aria-hidden="true">
      <path d="M0 0 H310 V18 L155 80 L0 18 Z" fill="var(--pink)"/>
      <path d="M0 140 L120 70 M310 140 L190 70" stroke="#eee" stroke-width="1" fill="none"/>
    </svg>
    <div class="brand"><span class="brand-mark"></span><span class="brand-name">LUMA CARE SERVICES</span></div>
  </section>

  <section class="item staff-card">
    <div class="brand light"><span class="brand-mark"></span><span class="brand-name">LUMA CARE SERVICES</span><span class="brand-tag">Kind support, every single day</span></div>
  </section>

  <section class="item biz-card">
    <div class="brand"><span class="brand-mark"></span><span class="brand-name">LUMA CARE SERVICES</span></div>
    <div class="biz-info">
      <div class="name">DANA WHITFIELD</div>
      <div class="role">Operating Manager</div>
      <div class="icon-row"><svg width="6" height="6" viewBox="0 0 10 10"><path d="M5 0a3.5 3.5 0 0 0-3.5 3.5C1.5 6 5 10 5 10s3.5-4 3.5-6.5A3.5 3.5 0 0 0 5 0z" fill="var(--pink-deep)"/></svg>48 Elm Ridge Road,<br>Northfield</div>
      <div class="icon-row"><svg width="6" height="6" viewBox="0 0 10 10"><path d="M2 0h2l1 3-1.5 1a6 6 0 0 0 2.5 2.5L7 5l3 1v2a2 2 0 0 1-2 2A8 8 0 0 1 0 2a2 2 0 0 1 2-2z" fill="var(--pink-deep)"/></svg>555 201 4410</div>
      <div class="icon-row"><svg width="6" height="6" viewBox="0 0 10 10"><path d="M2 0h2l1 3-1.5 1a6 6 0 0 0 2.5 2.5L7 5l3 1v2a2 2 0 0 1-2 2A8 8 0 0 1 0 2a2 2 0 0 1 2-2z" fill="var(--pink-deep)"/></svg>555 309 7722</div>
      <div class="icon-row"><svg width="6" height="6" viewBox="0 0 10 10"><rect x="0" y="2" width="10" height="7" fill="var(--pink-deep)"/></svg>team@lumacare.example</div>
      <div class="icon-row"><svg width="6" height="6" viewBox="0 0 10 10"><circle cx="5" cy="5" r="4.5" fill="var(--pink-deep)"/></svg>www.lumacare.example</div>
    </div>
    <div class="address-strip">Harbor Lane 1200 Elm Ridge Suite 18</div>
  </section>

  <section class="item sleeve">
    <div class="brand light"><span class="brand-mark"></span><span class="brand-name">LUMA CARE SERVICES</span><span class="brand-tag">Kind support, every single day</span></div>
  </section>

  <section class="item pencil-box">
    <div class="brand"><span class="brand-name">LUMA CARE SERVICES</span></div>
  </section>

  <section class="item wide-card">
    <div class="brand"><span class="brand-mark"></span><span class="brand-name">LUMA CARE SERVICES</span></div>
    <div class="wide-info">
      <div class="name">DANA WHITFIELD</div>
      <div>Co-Founder/Owner</div>
      <div>Elm Ridge Suite 18</div>
    </div>
    <div class="wide-right">
      <div class="icon-row"><svg width="6" height="6" viewBox="0 0 10 10"><path d="M2 0h2l1 3-1.5 1a6 6 0 0 0 2.5 2.5L7 5l3 1v2a2 2 0 0 1-2 2A8 8 0 0 1 0 2a2 2 0 0 1 2-2z" fill="var(--pink-deep)"/></svg>020 5550 0190</div>
      <div class="icon-row"><svg width="6" height="6" viewBox="0 0 10 10"><rect x="0" y="2" width="10" height="7" fill="var(--pink-deep)"/></svg>hello@lumacare.example</div>
      <div class="icon-row"><svg width="6" height="6" viewBox="0 0 10 10"><circle cx="5" cy="5" r="4.5" fill="var(--pink-deep)"/></svg>www.lumacare.example</div>
    </div>
    <div class="address-strip">Harbor Lane 1200 Elm Ridge Suite 18</div>
  </section>

  <section class="item bag">
    <svg class="wave" width="200" height="60" viewBox="0 0 200 60" aria-hidden="true">
      <path d="M0 0 H200 V30 C150 50 60 10 0 40 Z" fill="var(--pink)"/>
    </svg>
    <div class="brand"><span class="brand-mark"></span><span class="brand-name">LUMA CARE SERVICES</span><span class="brand-tag">Kind support, every single day</span></div>
    <div class="bag-contact left">555 201 4410<br>hello@lumacare.example</div>
    <div class="bag-contact right">48 Elm Ridge Road<br>Northfield</div>
    <div class="bag-slogan">GROW YOUR BUSINESS</div>
    <div class="bag-web">www.lumacare.example</div>
  </section>

</main>
</body>
</html>
```